Gaming Related Website

GuildWeave.com is a forum for gamers to connect online.

We would like a design for our front page.

Please feel free to include a basic logo.

Please take a look at the following sites for inspiration:
http://uk.plaryx.com/
http://eu.fraygrid.net/en/
http://www.stormvantor.com/

Target Market(s)

On-line gamers on consoles and PCs

Industry/Entity Type

Online

Requirements
Must have
• Please follow the wireframes attached.

```html
<!DOCTYPE html>
<html lang="en">
<head>
<meta charset="utf-8">
<title>GuildWeave.com – Gaming Social Network</title>
<link rel="stylesheet" href="https://fonts.googleapis.com/css2?family=Orbitron:wght@800&family=Oswald:wght@500&family=Arimo:wght@400;700&family=Montserrat:wght@600;700&display=swap">
<style>
:root{
  --bg:#121a26;
  --bg-top:#22324a;
  --shell:#0d131c;
  --panel:#19222f;
  --panel-dark:#111822;
  --line:#2a3443;
  --text:#e9edf2;
  --muted:#8a94a3;
  --orange:#f7a21b;
  --orange-dark:#e58a08;
  --blue:#1f63a6;
  --btn:#3a424d;
  --scroll:#2c3a4e;
}
*{box-sizing:border-box;margin:0;padding:0}
html,body{width:1200px;height:1070px;overflow:hidden}
body{position:relative;background:radial-gradient(ellipse 900px 260px at 560px 70px,var(--bg-top),transparent 70%),linear-gradient(var(--bg-top) 0,#17233a 200px,var(--bg) 420px,#0f1620 1070px);font-family:Arimo,Arial,sans-serif;color:var(--text)}
.abs{position:absolute}
.logo{left:126px;top:86px;font-family:Orbitron,sans-serif;font-weight:800;font-size:35px;color:var(--orange);letter-spacing:-1px}
.welcome{left:633px;top:84px;font-size:16.5px;line-height:23px;color:#fff;letter-spacing:-.3px}
.signup{left:980px;top:95px;width:101px;height:23px;background:var(--blue);color:#fff;font:700 10px Montserrat,sans-serif;display:flex;align-items:center;justify-content:center;border-radius:2px}
.nav{left:126px;top:230px;width:948px;display:flex;justify-content:space-between;font-family:Oswald,sans-serif;font-size:16px;color:#dfe3e8;text-transform:uppercase;letter-spacing:.2px}
.nav span{position:relative}
.nav span+span::before{content:"";position:absolute;left:-20px;top:-2px;height:26px;border-left:1px solid #3a4658}
.shell{left:115px;top:277px;width:972px;height:553px;background:var(--shell)}
.profile{left:121px;top:283px;width:244px;height:166px;background:var(--panel)}
.avatar{left:133px;top:299px;width:76px;height:72px;border:2px solid #33404f;background:linear-gradient(135deg,#6c4a32,#c08a5a 45%,#2a3d5c)}
.uname{left:221px;top:303px;font:600 11.5px Montserrat,sans-serif}
.plinks{left:221px;top:323px;font-size:9.5px;color:var(--orange);line-height:16px}
.plinks div::before{content:"";display:inline-block;width:8px;height:8px;background:var(--orange);margin-right:6px;vertical-align:-1px;border-radius:1px}
.stat{top:383px;width:80px;text-align:center}
.stat b{display:block;font:800 27px Orbitron,sans-serif;color:var(--orange)}
.stat small{font:700 9px Montserrat,sans-serif;color:#fff}
.statsep{top:390px;height:38px;border-left:1px solid #2e3a4a}
.games{left:121px;top:455px;width:244px;height:375px;background:var(--panel)}
.btn-orange{background:var(--orange);color:#1a1a1a;font:700 9.5px Montserrat,sans-serif;display:flex;align-items:center;justify-content:center;text-transform:uppercase}
.gamelist{left:127px;top:492px;width:208px;list-style:none}
.gamelist li{height:37.5px;border-top:1px solid var(--line);font:600 9.5px Montserrat,sans-serif;display:flex;align-items:center;justify-content:space-between;padding:0 4px 0 10px;text-transform:uppercase}
.gamelist li::after{content:"";width:6px;height:6px;border-right:2px solid #6a7585;border-top:2px solid #6a7585;transform:rotate(45deg)}
.scroll{width:6px;background:var(--scroll);border-radius:3px}
.tabs{height:30px;display:flex;align-items:center;font:700 9.5px Montserrat,sans-serif;text-transform:uppercase}
.tabs .on{color:var(--orange);background:var(--panel);height:30px;display:flex;align-items:center;padding:0 16px}
.tabs span{padding:0 16px}
.feed{left:372px;top:283px;width:466px;height:547px;background:var(--panel)}
.filter{left:390px;top:327px;font-size:11px;display:flex;gap:10px;align-items:center}
.filter b{font:700 9.5px Montserrat,sans-serif;margin-right:32px}
.chk::before{content:"✓";display:inline-block;width:10px;height:10px;background:var(--orange);color:#111;font-size:8px;line-height:10px;text-align:center;margin-right:6px;vertical-align:-1px}
.items{left:380px;top:363px;width:432px;list-style:none;font-size:12px;line-height:22px}
.items li{border-bottom:1px solid var(--line);padding:7px 9px}
.items a{color:var(--orange);text-decoration:none}
.acts{display:flex;gap:5px;margin-top:2px}
.acts span{background:var(--btn);font-size:9px;padding:0 14px;height:20px;line-height:20px}
.side{width:234px;background:var(--panel)}
.rows{list-style:none;font-size:11px}
.rows li{height:22px;display:flex;align-items:center}
.srv li span:nth-child(1){width:116px}
.srv li span:nth-child(2){width:48px}
.join{background:var(--btn);font-size:8px;padding:1px 4px}
.com li span:first-child{width:132px;color:var(--orange)}
.sidefoot{background:#1f2a3a}
.fhead{top:859px;font:700 14px Montserrat,sans-serif;display:flex;align-items:center;gap:8px;letter-spacing:.5px}
.fhead i{width:20px;height:14px;background:var(--orange);border-radius:3px}
.fhr{left:121px;width:951px;border-top:1px solid #2a3442}
.flist{top:900px;list-style:none;font-size:9.5px;line-height:16px;color:var(--muted);text-transform:uppercase}
.flist em{font-style:normal;color:var(--orange);font-weight:700;margin-right:8px}
.follow{left:857px;top:904px;width:209px;height:82px;background:#1c2431;padding:12px 16px}
.follow h4{font:600 14px Montserrat,sans-serif;color:#c7ccd3;display:flex;align-items:center;gap:6px}
.follow h4 i{width:21px;height:21px}
.follow p{font-size:10.5px;color:#c0c6cf;line-height:15px;margin-top:8px}
.bottom{top:1028px;font-size:9.5px;color:var(--muted);text-transform:uppercase;display:flex;gap:14px}
.copy{left:851px;top:1028px;font-size:9.5px;color:#c7ccd3}
</style>
</head>
<body>
<header>
  <div class="abs logo">GUILDWEAVE.COM</div>
  <p class="abs welcome">Welcome to GuildWeave gaming social network.<br>Join thousands of players online today.</p>
  <div class="abs signup">SIGN UP NOW</div>
  <nav class="abs nav"><span>Headlines</span><span>Forum</span><span>Communities</span><span>Challenges</span><span>Games Info &amp; Downloads</span><span>Competitions</span><span>Achievements</span><span>Teams</span></nav>
</header>

<main>
  <div class="abs shell"></div>

  <section class="abs profile"></section>
  <div class="abs avatar" role="img" aria-label="Player avatar portrait"></div>
  <div class="abs uname">LAZY GOURMET</div>
  <div class="abs plinks"><div>Edit</div><div>Logout</div><div>Gaming Stats</div></div>
  <div class="abs stat" style="left:120px"><b>16</b><small>GAMES</small></div>
  <div class="abs statsep" style="left:200px"></div>
  <div class="abs stat" style="left:207px"><b>3</b><small>COMMUNITIES</small></div>
  <div class="abs statsep" style="left:294px"></div>
  <div class="abs stat" style="left:289px"><b>2</b><small>TEAMS</small></div>

  <section class="abs games"></section>
  <div class="abs btn-orange" style="left:179px;top:462px;width:124px;height:22px">All Games</div>
  <ul class="abs gamelist">
    <li>Borderfall II</li><li>Shadowblade III</li><li>Line of Fire: Dark Ops 2</li><li>Clan Feuds II</li><li>Badge of Valor Warfighter</li><li>Realm of Spellcraft</li><li>Far Reach</li><li>Borderfall II</li><li>Shadowblade III</li>
  </ul>
  <div class="abs scroll" style="left:351px;top:462px;height:198px"></div>

  <section class="abs feed">
    <div class="tabs" style="background:var(--shell)"><span class="on">Newsfeed</span><span>Chats</span></div>
  </section>
  <div class="abs filter"><b>FILTER BY:</b><span class="chk">Notifications</span><span class="chk">Communities</span><span class="chk" style="color:var(--muted)">Teams</span><span class="chk">Competitions</span></div>
  <ul class="abs items">
    <li>You have been challenged by pokri for a 1v1 game og Tremor Live at 12:30, Today<div class="acts"><span>CANCEL</span><span>ACCEPT</span></div></li>
    <li>New patch is out for Realm of Spellcraft <a>Read more</a></li>
    <li style="padding:11px 9px">Mini has posted in the &nbsp;«<a>Team Hot Shots</a> » Private Board</li>
    <li>You’ve been invited to join <a>50 Klicks Gaming community</a><div class="acts"><span>CANCEL</span><span>ACCEPT</span></div></li>
    <li style="padding:9px 9px">The Next GQ WG3 match in WG3 4v4 Ladder has been canceled</li>
    <li style="padding:10px 9px">Your application to join stars of 50k teams has been accepted</li>
    <li style="padding:10px 9px"><a>Hidden1</a> has accepted the invitation to become an admin of VS3 Mini League</li>
    <li style="padding:10px 9px"><a>Team 1337</a> Players has won against 50k stars in WG3 4v4 S&amp;D Ladder</li>
    <li style="border:0;padding:10px 9px">The Next GQ WG3 match in WG3 4v4 Ladder has been canceled</li>
  </ul>
  <div class="abs scroll" style="left:823px;top:363px;height:199px"></div>

  <section class="abs side" style="left:845px;top:283px;height:272px">
    <div class="tabs" style="background:var(--shell)"><span class="on" style="padding:0 12px">Game Servers</span><span>Voip Channels</span></div>
    <ul class="rows srv" style="padding:16px 0 0 12px">
      <li><span>Warground 3</span><span>12 | 34</span><span class="join">JOIN</span></li>
      <li><span>Far Reach</span><span>34 | 34</span><span class="join">JOIN</span></li>
      <li><span>Shadowblade III</span><span>15 |15</span></li>
      <li><span>Clan Feuds II</span><span>12 | 34</span><span class="join">JOIN</span></li>
      <li><span>Badge of Valor</span><span>34 | 34</span><span class="join">JOIN</span></li>
      <li><span>Warground 3</span><span>15 |15</span></li>
      <li><span>Far Reach</span><span>12 | 34</span><span class="join">JOIN</span></li>
      <li><span>Shadowblade III</span><span>34 | 34</span><span class="join">JOIN</span></li>
    </ul>
  </section>
  <div class="abs sidefoot" style="left:845px;top:519px;width:234px;height:36px"></div>
  <div class="abs btn-orange" style="left:905px;top:527px;width:124px;height:21px">Set up a server</div>
  <div class="abs scroll" style="left:1065px;top:322px;height:118px"></div>

  <section class="abs side" style="left:845px;top:562px;height:268px">
    <div class="tabs" style="background:var(--shell)"><span class="on" style="padding:0 14px">My Communities</span><span style="padding:0 12px">My Teams</span></div>
    <ul class="rows com" style="padding:11px 0 0 13px;font-size:11.5px">
      <li><span>PlayQuorix.com</span><span>8 Online</span></li>
      <li><span>Tacticrew.com</span><span>10 Online</span></li>
      <li><span>Gamerzlink.com</span><span>20 Online</span></li>
      <li><span>PlayQuorix.com</span><span>5 Online</span></li>
      <li><span>Tacticrew.com</span><span>6 Online</span></li>
      <li><span>Gamerzlink.com</span><span>7 Online</span></li>
      <li><span>PlayQuorix.com</span><span>10 Online</span></li>
      <li><span>Tacticrew.com</span><span>12 Online</span></li>
    </ul>
  </section>
  <div class="abs sidefoot" style="left:845px;top:795px;width:234px;height:35px"></div>
  <div class="abs btn-orange" style="left:898px;top:803px;width:140px;height:22px">Set up a community</div>
  <div class="abs scroll" style="left:1065px;top:598px;height:118px"></div>
</main>

<footer>
  <div class="abs fhead" style="left:123px"><i></i>GAMES</div>
  <div class="abs fhead" style="left:378px"><i style="width:16px"></i>COMMUNITY</div>
  <div class="abs fhead" style="left:614px"><i></i>TEAMS</div>
  <div class="abs fhr" style="top:884px"></div>
  <ul class="abs flist" style="left:123px"><li><em>34</em>Borderfall II</li><li><em>56</em>Shadowblade III</li><li><em>23</em>Line of Fire: Dark Ops 2</li><li><em>78</em>Clan Feuds II</li><li><em>23</em>Badge of Valor Warfighter</li><li><em>19</em>Realm of Spellcraft</li></ul>
  <ul class="abs flist" style="left:377px"><li>Borderfall II</li><li>Shadowblade III</li><li>Line of Fire: Dark Ops 2</li><li>Clan Feuds II</li><li>Badge of Valor Warfighter</li><li>Realm of Spellcraft</li></ul>
  <ul class="abs flist" style="left:615px"><li>Borderfall II</li><li>Shadowblade III</li><li>Line of Fire: Dark Ops 2</li><li>Clan Feuds II</li><li>Badge of Valor Warfighter</li><li>Realm of Spellcraft</li></ul>
  <div class="abs follow">
    <h4>FOLLOW US:<i style="background:#3b5a9a;margin-left:6px"></i><i style="background:#2aa3d8"></i><i style="background:#5a5f66"></i></h4>
    <p>Lorem ipsum dolor sit amet, conse ctetur adipisicing elit, sed do eius</p>
  </div>
  <div class="abs fhr" style="top:1012px"></div>
  <nav class="abs bottom" style="left:125px"><span>Termsof Use</span><span>Legal</span><span>Privacy Policy</span><span>Support</span><span>Contact Us</span></nav>
  <div class="abs copy">Copyright © 2012 GuildWeave. All Rights Reserved.</div>
</footer>
</body>
</html>
```